2 x Digitize Logo | 2 x Business Cards | 2 x Fridge Magnets

We require 6 deliverables:
1. Residential logo redrawn (same just high quality for large print format).
2. Corporate logo redrawn (minor changes to wording and high quality for large print format).
3. New business card design for Furniture Removals (residential)
4. New business card design for Corporate Relocations (business)
5. New Fridge magnet for Furniture removals (residential)
6. New fridge magnet for Corporate Relocations (business)
1. Residential Logo
a. We require the logo to be translated into a high quality digital image with no modifications.
(see attached resilogo.jpg)
2. Residential Logo
a. We require the logo to be edited (add the word corporate relocations) be translated into a high quality digital image.
(see attached corplogo.jpg)
3. Using the resilogo please make a new business card for our business.
a. Please see the web site https://www.bluegatehaulage.com.au for colours and inspiration.
b. The residential business card needs the following information:
i. Business Name (using the residential logo).
ii. Free Call: 1800 BG Haul (the B, G and Haul much be the same colour as the logo).
iii. Website: www.BluegateHaulage.com.au
iv. Address: 4/6 Marlow Court, VIC 3201
v. Email: move@BluegateHaulage.com.au
vi. backof Card:
Review our service
www.TellTallyHub.com.au
Services: Local, Country, Interstate | Furniture Removals | Piano, Billiard Tables & Antiques
4. Using the corplogo please make a new business card for our business.
b. The corporate business card needs the following information:
i. Business Name (using the corporate logo).
v. Email: corporate@BluegateHaulage.com.au
vi. Back of Card:
Review our service
www.TellTallyHub.com.au
Services: Corporate relocations | Office equipment moves | Packing Service | Packing Materials
5. Using the resilogo please make a new fridge magent for our business.
b. The residential fidge magnet needs the following information:
iv. Services: Local, Country, Interstate | Furniture Removals | Piano, Billiard Tables & Antiques
6. Using the corplogo please make a new fridge magent for our business.
b. The corporate fidge magnet needs the following information:
iv. Services: Local, Country, Interstate | Corporate relocations
Target Market(s)
Residential Furniture Removals and Corporate Office relocations
Industry/Entity Type
Business
Contact Information for Business Card
Please see full brief for six items required
Requirements
Must have
- Clean simple, easy to read
Nice to have
- fresh, stand out, eye catching
Should not have
- plain, standard, boring, general

```html
<!DOCTYPE html>
<html lang="en">
<head>
<meta charset="utf-8">
<title>Bluegate Haulage – Corporate Business Card</title>
<link rel="stylesheet" href="https://fonts.googleapis.com/css2?family=Roboto+Condensed:wght@700&display=swap">
<style>
  :root {
    --ink: #333333;
    --paper: #ffffff;
    --brand-red: #e9343a;
    --brand-green: #00a651;
    --brand-yellow: #fdc010;
    --frame: #333333;
  }
  * { margin: 0; padding: 0; box-sizing: border-box; }
  html, body {
    width: 1200px;
    height: 1200px;
    overflow: hidden;
    background: var(--paper);
  }
  body {
    font-family: "Roboto Condensed", "Arial Narrow", sans-serif;
    font-weight: 700;
    color: var(--ink);
  }
  .canvas {
    position: relative;
    width: 1200px;
    height: 1200px;
    border: 2px solid var(--frame);
  }
  .card {
    position: absolute;
    left: 185px;
    width: 830px;
    height: 460px;
    border: 1.6px solid var(--frame);
    background: var(--paper);
  }
  .card--front { top: 133px; }
  .card--back { top: 605px; }

  .brand {
    position: absolute;
    top: 150px;
    right: 60px;
    display: flex;
    align-items: center;
    gap: 14px;
    font-size: 40px;
    line-height: 1;
    color: var(--brand-red);
  }
  .brand__mark {
    width: 30px;
    height: 30px;
    background: var(--brand-green);
  }

  .contact {
    position: absolute;
    left: 43px;
    top: 251px;
    line-height: 1;
  }
  .contact__freecall {
    font-size: 48px;
    letter-spacing: -0.3px;
    margin-bottom: 12px;
  }
  .accent-yellow { color: var(--brand-yellow); }
  .accent-red { color: var(--brand-red); }
  .accent-green { color: var(--brand-green); }
  .contact__line {
    font-size: 31px;
    margin-bottom: 10px;
  }

  .review {
    position: absolute;
    left: 0;
    right: 0;
    top: 76px;
    text-align: center;
    font-size: 46px;
    line-height: 66px;
  }
  .services {
    position: absolute;
    left: 0;
    right: 0;
    top: 272px;
    text-align: center;
    line-height: 1;
  }
  .services__title {
    font-size: 31px;
    margin-bottom: 30px;
  }
  .services__list {
    font-size: 32px;
    line-height: 44px;
  }
</style>
</head>
<body>
  <main class="canvas">
    <section class="card card--front" aria-label="Business card front">
      <div class="brand">
        <span class="brand__mark" aria-hidden="true"></span>
        <span class="brand__name">Bluegate Haulage</span>
      </div>
      <div class="contact">
        <p class="contact__freecall">Free Call: 1800 <span class="accent-yellow">B</span><span class="accent-red">G</span> <span class="accent-green">Haul</span></p>
        <p class="contact__line">Website: www.BluegateHaulage.com.au</p>
        <p class="contact__line">Adress: 4/6 Marlow Court, VIC 3201</p>
        <p class="contact__line">Email: corporate@BluegateHaulage.com.au</p>
      </div>
    </section>

    <section class="card card--back" aria-label="Business card back">
      <div class="review">
        <p>Review our service</p>
        <p>www.TellTallyHub.com.au</p>
      </div>
      <div class="services">
        <p class="services__title">Services:</p>
        <p class="services__list">Corporate relocations | Office equipment moves<br>Packing Service | Packing Materials</p>
      </div>
    </section>
  </main>
</body>
</html>
```